I would like a stylish low key card that represents my Cedar Lodge. A boutique rental property . This property is of the highest standard and I wish the card to covey this without being old fashion

Industry/Entity Type

Boutique

Contact Information for Business Card

Tess Varlowe
0438207519
tess.varlowe@varlowe.com.au Cedar Lodge

```html
<!DOCTYPE html>
<html lang="en">
<head>
<meta charset="utf-8">
<title>The Cedar Lodge – Business Card</title>
<link rel="stylesheet" href="https://fonts.googleapis.com/css2?family=Playfair+Display:wght@400&display=swap">
<style>
  :root {
    --card-grey: #9a9b9f;
    --ink-white: #ffffff;
    --ink-black: #141414;
    --serif: "Playfair Display", "Didot", serif;
  }
  html, body {
    margin: 0;
    padding: 0;
    overflow: hidden;
    background: var(--card-grey);
  }
  .card {
    position: relative;
    width: 1200px;
    height: 693px;
    background: var(--card-grey);
    font-family: var(--serif);
    overflow: hidden;
  }
  .brand-mark {
    position: absolute;
    left: 477px;
    top: 148px;
    width: 246px;
    height: 246px;
  }
  .business-name {
    position: absolute;
    left: 0;
    right: 0;
    top: 388px;
    margin: 0;
    text-align: center;
    font-weight: 400;
    font-size: 78px;
    line-height: 1;
    color: var(--ink-white);
    letter-spacing: 0.5px;
  }
  .contact-name {
    position: absolute;
    left: 0;
    right: 0;
    top: 487px;
    margin: 0;
    text-align: center;
    font-weight: 400;
    font-size: 38px;
    line-height: 1;
    color: var(--ink-black);
  }
  .contact-details {
    position: absolute;
    left: 0;
    right: 0;
    top: 542px;
    margin: 0;
    text-align: center;
    font-size: 26px;
    line-height: 1;
    color: var(--ink-black);
  }
</style>
</head>
<body>
  <main class="card">
    <svg class="brand-mark" viewBox="0 0 246 246" aria-hidden="true">
      <circle cx="123" cy="123" r="118" fill="var(--ink-white)" stroke="var(--ink-black)" stroke-width="6"/>
    </svg>
    <h1 class="business-name">The Cedar Lodge</h1>
    <p class="contact-name">Tess Varlowe</p>
    <p class="contact-details">0438207519 | tess.varlowe@varlowe.com.au</p>
  </main>
</body>
</html>
```